Business card design needed

We require a business card and logo design for our tipper truck business which services the building and agricultural industries, based in Albury-Wodonga, Australia. The business name is 'Falcon Haulage' and our business moto is 'if it's tippable, it's doable'.
If a tipper truck is to be included in the logo, the truck must not have a nose ie. the truck must have a flat front.
The moto for the Albury-Wodonga region is 'where the mountains meet the murray' (snowy mountains meet murray river-this may or may not be included in the image design)

Industry/Entity Type

Building

Contact Information for Business Card

FALCON HAULAGE PTY LTD
Complete Dumping Solutions
Load it up, we'll move it out!
Col Brimble
0483 906 217
falconhaulage@quillmail.com.au
PO Box 829
Fernvale NSW 2739
ABN: 57 309 842 615

```html
<!DOCTYPE html>
<html lang="en">
<head>
<meta charset="utf-8">
<title>Falcon Haulage – Business Card</title>
<link rel="stylesheet" href="https://fonts.googleapis.com/css2?family=Lexend:wght@300;800&family=Source+Sans+3:ital,wght@0,400;0,600;0,700;1,400&display=swap">
<style>
  :root {
    --brand-blue: #00aeef;
    --ink: #111111;
    --black: #000000;
    --white: #ffffff;
    --grey-text: #8a8a8a;
    --stage-dark: #0a0a0a;
    --stage-mid: #6e6e70;
    --photo-yellow: #f2c21b;
    --photo-shade: #e6e6e6;
  }
  * { margin: 0; padding: 0; box-sizing: border-box; }
  html, body { width: 1200px; height: 900px; overflow: hidden; }
  body {
    position: relative;
    background: linear-gradient(90deg, var(--stage-dark) 0%, var(--stage-mid) 50%, var(--stage-dark) 100%);
    font-family: "Source Sans 3", sans-serif;
  }
  .card { position: absolute; left: 252px; width: 696px; overflow: hidden; }

  /* Front */
  .card--front { top: 17px; height: 426px; background: var(--white); }
  .front-header {
    position: absolute; left: 0; top: 0; width: 100%; height: 142px;
    background: var(--black);
  }
  .front-rule {
    position: absolute; left: 0; top: 146px; width: 100%; height: 10px;
    background: var(--black);
  }
  .brand-mark {
    position: absolute; left: 52px; top: 52px; width: 40px; height: 40px;
    border-radius: 50%; background: var(--brand-blue);
  }
  .brand-name {
    position: absolute; left: 118px; top: 62px;
    font-weight: 700; font-size: 27px; color: var(--brand-blue); letter-spacing: 0.2px;
    white-space: nowrap;
  }
  .brand-service {
    position: absolute; left: 0; width: 626px; top: 98px; text-align: center;
    font-size: 20px; color: var(--white);
  }
  .person-name {
    position: absolute; left: 38px; top: 192px;
    font-family: "Lexend", sans-serif; font-size: 31px; line-height: 1; white-space: nowrap;
  }
  .person-name__first { font-weight: 300; color: var(--ink); }
  .person-name__last { font-weight: 800; color: var(--brand-blue); margin-left: 10px; }
  .person-role {
    position: absolute; left: 38px; top: 226px;
    font-weight: 700; font-size: 17px; color: var(--grey-text);
  }
  .contact-list {
    position: absolute; left: 38px; top: 298px; list-style: none;
    font-size: 18px; color: var(--ink); line-height: 28px;
  }
  .contact-list li { display: flex; align-items: center; height: 28px; }
  .contact-list svg { width: 22px; height: 22px; margin-right: 8px; flex: none; }
  .contact-list .no-icon { padding-left: 30px; }
  .photo-area {
    position: absolute; left: 318px; top: 252px; width: 378px; height: 174px;
    background: linear-gradient(90deg, var(--white) 0%, var(--photo-shade) 12%, var(--photo-yellow) 30%, var(--photo-yellow) 88%, #e0b010 100%);
  }
  .tagline {
    position: absolute; right: 30px; top: 210px;
    font-style: italic; font-size: 25px; color: var(--brand-blue); white-space: nowrap;
  }

  /* Back */
  .card--back {
    top: 460px; height: 425px; background: var(--brand-blue);
    display: flex; align-items: center; justify-content: center;
  }
  .back-tagline { font-style: italic; font-size: 26px; color: var(--ink); margin-top: 2px; }
</style>
</head>
<body>
  <section class="card card--front">
    <header class="front-header">
      <span class="brand-mark"></span>
      <div class="brand-name">FALCON HAULAGE PTY LTD</div>
      <div class="brand-service">Complete Dumping Solutions</div>
    </header>
    <div class="front-rule"></div>

    <div class="person-name"><span class="person-name__first">Col</span><span class="person-name__last">Brimble</span></div>
    <div class="person-role">Managing Director</div>

    <div class="photo-area" role="img" aria-label="Photo of a yellow tipper truck with a flat front"></div>
    <div class="tagline">Load it up, we'll move it out!</div>

    <ul class="contact-list">
      <li>
        <svg viewBox="0 0 22 22" aria-hidden="true"><rect x="6" y="1" width="10" height="20" rx="2" fill="none" stroke="var(--brand-blue)" stroke-width="2"/><rect x="8" y="4" width="6" height="11" fill="var(--brand-blue)"/></svg>
        0483 906 217
      </li>
      <li>
        <svg viewBox="0 0 22 22" aria-hidden="true"><rect x="1" y="4" width="20" height="14" fill="none" stroke="var(--brand-blue)" stroke-width="2"/><path d="M1 4 L11 12 L21 4 M1 18 L8.5 10 M21 18 L13.5 10" fill="none" stroke="var(--brand-blue)" stroke-width="2"/></svg>
        falconhaulage@quillmail.com.au
      </li>
      <li>
        <svg viewBox="0 0 22 22" aria-hidden="true"><path d="M11 22 C11 22 3 12 3 8 A8 8 0 0 1 19 8 C19 12 11 22 11 22 Z" fill="var(--brand-blue)"/></svg>
        PO Box 829 Fernvale NSW 2739
      </li>
      <li class="no-icon">ABN: 57 309 842 615</li>
    </ul>
  </section>

  <section class="card card--back">
    <p class="back-tagline">Load it up, we'll move it out!</p>
  </section>
</body>
</html>
```